Investment Business - Biz Card Design

Using the attached logo files, please create a superior business card design for Tarnwell Holdings.

The "back" of the card should feature the logo (either in colour, or white/black over a feature colour)

The "front" of the card should feature: name, email, and phone

The design should be minimal and clean.

Target Market(s)

Business owners who need our investment services.

Industry/Entity Type

Business

```html
<!DOCTYPE html>
<html lang="en">
<head>
<meta charset="utf-8">
<title>Tarnwell Holdings – Business Card</title>
<link href="https://fonts.googleapis.com/css2?family=Montserrat:wght@700&family=Open+Sans:wght@400;600&display=swap" rel="stylesheet">
<style>
  :root {
    --stage: #e6e7ea;
    --card: #ffffff;
    --navy: #2b2a82;
    --sky: #3a9fdc;
    --ink: #2a2a2a;
    --rule: #c9d6e6;
  }
  * { box-sizing: border-box; margin: 0; padding: 0; }
  html, body { width: 1200px; height: 951px; overflow: hidden; }
  body { background: var(--stage); position: relative; font-family: "Open Sans", sans-serif; }

  .card {
    position: absolute;
    width: 600px; height: 343px;
    background: var(--card);
    border-radius: 22px;
    overflow: hidden;
    box-shadow: 0 10px 28px rgba(0,0,0,.18);
  }
  .card--back { left: 90px; top: 80px; }
  .card--front { left: 510px; top: 520px; }

  .wordmark {
    display: flex; align-items: center; gap: 14px;
    font-family: "Montserrat", sans-serif; font-weight: 700;
    color: var(--navy); letter-spacing: .5px; white-space: nowrap;
  }
  .wordmark__dot { width: 16px; height: 16px; background: var(--navy); border-radius: 50%; flex: none; }

  .card--back .wordmark { position: absolute; left: 70px; top: 118px; font-size: 40px; }
  .card--back .website {
    position: absolute; left: 0; right: 0; bottom: 48px;
    text-align: center; font-size: 17px; font-weight: 600; color: var(--ink); letter-spacing: .4px;
  }

  .card--front .wordmark { position: absolute; left: 36px; top: 128px; font-size: 24px; gap: 10px; }
  .card--front .wordmark__dot { width: 11px; height: 11px; }
  .divider {
    position: absolute; left: 300px; top: 36px; width: 1px; height: 220px;
    background: linear-gradient(var(--card), var(--rule) 20%, var(--rule) 80%, var(--card));
  }
  .contact { position: absolute; left: 318px; top: 44px; color: var(--ink); }
  .contact__name { font-size: 19px; font-weight: 600; letter-spacing: .3px; }
  .contact__role { font-size: 13px; color: var(--sky); margin-bottom: 26px; }
  .contact__row { display: flex; gap: 10px; font-size: 15px; line-height: 19px; }
  .contact__row svg { width: 14px; height: 14px; margin-top: 2px; flex: none; fill: var(--sky); }
  .contact__address { margin-bottom: 18px; }
  .contact__web { font-weight: 600; }

  .band-line { position: absolute; left: 0; right: 0; bottom: 44px; height: 2px; background: var(--sky); }
  .band { position: absolute; left: 0; right: 0; bottom: 0; height: 40px; background: var(--navy); }
</style>
</head>
<body>

<section class="card card--back" aria-label="Card back">
  <div class="wordmark"><span class="wordmark__dot"></span>Tarnwell Holdings</div>
  <p class="website">www.tarnwell.com</p>
</section>

<section class="card card--front" aria-label="Card front">
  <div class="wordmark"><span class="wordmark__dot"></span>Tarnwell Holdings</div>
  <div class="divider"></div>
  <div class="contact">
    <p class="contact__name">Marcus Ellery</p>
    <p class="contact__role">director</p>
    <div class="contact__row contact__address">
      <svg viewBox="0 0 16 16"><path d="M8 1 1 7.5h2V15h4v-4h2v4h4V7.5h2z"/></svg>
      <span>2750 Larkspur Ln<br>Dellton, TX 78110</span>
    </div>
    <div class="contact__row">
      <svg viewBox="0 0 16 16"><path d="M4 1 6.5 4 5 6c1 2 3 4 5 5l2-1.5L15 12l-2 3C7 14 2 9 1 3z"/></svg>
      <span>512-555-0140</span>
    </div>
    <div class="contact__row">
      <svg viewBox="0 0 16 16"><path d="M3 1h7v4H3zM1 6h14v6h-2v3H3v-3H1zM5 10v3h6v-3z"/></svg>
      <span>512-555-0141</span>
    </div>
    <div class="contact__row">
      <svg viewBox="0 0 16 16"><path d="M1 3h14v10H1zm1.5 1.5L8 9l5.5-4.5z"/></svg>
      <span>info@tarnwell.com</span>
    </div>
    <div class="contact__row contact__web">
      <svg viewBox="0 0 16 16"><circle cx="8" cy="8" r="7"/></svg>
      <span>www.tarnwell.com</span>
    </div>
  </div>
  <div class="band-line"></div>
  <div class="band"></div>
</section>

</body>
</html>
```